2957 Corliss Road Medical Centre

We are looking for a design for new medical clinic.
We are accepting new patients at this new medical centre grand opening. Walk-ins are welcome.
Our cardiac and vascular surgical specialists are department heads at Brenwood Vale Hospital, a leading teaching hospital in Toronto. These specialists will see cardiovascular consults are well as pre-surgical and post-surgical consultations and follow-ups.
Our lab is affiliated with several nuclear medicine clinics in the GTA.
Our Services Includes:
Family Practice
Cardiology Diagnostics
Cardiac & Vascular Surgical Consultation
Ultrasound & Vascular Testing
Open 6 days a week.
Ample Free Parking
Friendly Staffs

Target Market(s)

New Patients. Families of any age. Ethnic groups including Asians & Africans.

Industry/Entity Type

Medical

Font styles to use
Serif
Sans Serif
Decorative
Script
Other font styles liked:
• Arial calibri, verdana

Requirements
Must have
• Address:
• 2957 Corliss Road West
• Unit 418
• Scarborough, Ontario
• K7P 2H9
• Tel: (555) 384-2760
Nice to have
• Caring and inviting environment.
• Simple but classy.
• Standout colors.
Should not have
• Busy images. Aside from this, any ideas are welcome.

```html
<!DOCTYPE html>
<html lang="en">
<head>
<meta charset="utf-8">
<title>Grand Opening – New Medical Clinic</title>
<link rel="stylesheet" href="https://fonts.googleapis.com/css2?family=Great+Vibes&family=Arimo:wght@700&family=Roboto+Condensed:wght@700&family=Open+Sans:wght@400&family=Montserrat:wght@300&family=Lato:wght@700&display=swap">
<style>
  :root {
    --paper: #f7f7f8;
    --paper-shade: #ececee;
    --gold: #f7d917;
    --gold-dark: #c79a06;
    --blue: #0d6cc0;
    --blue-deep: #0a4f9c;
    --blue-light: #3d9be6;
    --yellow: #ffd500;
    --yellow-deep: #f2b700;
    --green: #8cc63f;
    --green-deep: #6aa72a;
    --rule: #b8b1a2;
    --ink: #1b1b1b;
    --list-rule: #c9c9c9;
    --photo-top: #dfe6ec;
    --photo-mid: #eef2f5;
  }
  * { box-sizing: border-box; margin: 0; padding: 0; }
  html, body { width: 975px; height: 1200px; overflow: hidden; }
  body { background: #ffffff; }

  .flyer {
    position: relative;
    width: 975px;
    height: 1200px;
    background: radial-gradient(ellipse at 50% 40%, var(--paper) 0%, var(--paper-shade) 100%);
    overflow: hidden;
  }

  .headline-script {
    position: absolute;
    top: 40px; left: 0; width: 100%;
    text-align: center;
    font-family: "Great Vibes", cursive;
    font-size: 132px;
    line-height: 1;
    color: var(--gold);
    text-shadow: 1px 2px 0 var(--gold-dark), 2px 4px 5px rgba(0,0,0,0.25);
  }

  .headline-main {
    position: absolute;
    left: 0; width: 100%;
    text-align: center;
    font-family: "Arimo", Arial, sans-serif;
    font-weight: 700;
    line-height: 1;
    letter-spacing: -2px;
    background: linear-gradient(180deg, var(--blue-light) 0%, var(--blue) 50%, var(--blue-deep) 100%);
    -webkit-background-clip: text;
    background-clip: text;
    color: transparent;
    filter: drop-shadow(2px 3px 2px rgba(0,0,0,0.25));
  }
  .headline-main.line-one { top: 218px; font-size: 106px; }
  .headline-main.line-two { top: 320px; font-size: 132px; }

  .connector-lines { position: absolute; top: 596px; left: 0; }

  .badge {
    position: absolute;
    top: 478px;
    width: 268px; height: 268px;
    border-radius: 50%;
    display: flex; align-items: center; justify-content: center;
    text-align: center;
    font-family: "Roboto Condensed", "Arial Narrow", sans-serif;
    font-weight: 700;
    color: #ffffff;
    box-shadow: 3px 6px 10px rgba(0,0,0,0.3);
    text-shadow: 2px 2px 3px rgba(0,0,0,0.35);
  }
  .badge-yellow { left: 55px; background: radial-gradient(circle at 40% 30%, #ffe869 0%, var(--yellow) 45%, var(--yellow-deep) 100%); font-size: 49px; line-height: 1.05; }
  .badge-blue { left: 349px; background: radial-gradient(circle at 40% 30%, var(--blue-light) 0%, var(--blue) 50%, var(--blue-deep) 100%); font-size: 52px; line-height: 1.08; }
  .badge-green { left: 647px; background: radial-gradient(circle at 40% 30%, #b4df6f 0%, var(--green) 50%, var(--green-deep) 100%); font-size: 47px; line-height: 1.07; }

  .doctor-photo {
    position: absolute;
    z-index: 1;
    left: 318px; top: 762px; width: 272px; height: 391px;
    background:
      linear-gradient(90deg, rgba(238,238,240,1) 0%, rgba(238,238,240,0) 30%),
      linear-gradient(180deg, var(--photo-top) 0%, var(--photo-mid) 45%, #f4f6f8 100%);
    border-radius: 120px 120px 0 0;
  }

  .services {
    position: absolute;
    z-index: 2;
    left: 44px; top: 806px; width: 310px;
    font-family: "Open Sans", Calibri, sans-serif;
    text-align: center;
  }
  .services-title {
    font-family: "Lato", Arial, sans-serif;
    font-weight: 700;
    font-size: 29px;
    color: var(--blue);
    margin-bottom: 13px;
    letter-spacing: 0.2px;
  }
  .services-list { list-style: none; font-size: 20px; color: var(--ink); line-height: 1.3; }
  .services-list li { padding: 6px 0 8px; border-bottom: 1px solid var(--list-rule); }
  .services-list li:last-child { border-bottom: none; }

  .location {
    position: absolute;
    z-index: 2;
    left: 584px; top: 797px; width: 337px;
    text-align: center;
  }
  .location-title {
    font-family: "Montserrat", Arial, sans-serif;
    font-weight: 300;
    font-size: 26px;
    color: var(--blue);
    letter-spacing: 1px;
    padding-bottom: 6px;
    border-bottom: 1px solid #555;
  }
  .location-address {
    font-family: "Lato", Calibri, sans-serif;
    font-weight: 700;
    font-size: 22px;
    line-height: 1.7;
    color: var(--ink);
    padding: 8px 0 6px;
    border-bottom: 1px solid #555;
  }

  .booking {
    position: absolute;
    z-index: 2;
    left: 584px; top: 988px; width: 337px;
    text-align: center;
    font-family: "Roboto Condensed", "Arial Narrow", sans-serif;
    font-weight: 700;
  }
  .booking-call { font-size: 45px; line-height: 1.02; color: var(--blue); }
  .booking-phone { font-size: 50px; line-height: 1.1; color: var(--ink); margin-top: 4px; }

  .footer-band {
    position: absolute;
    z-index: 3;
    left: 0; bottom: 0; width: 100%; height: 50px;
    background: linear-gradient(180deg, var(--blue-light) 0%, var(--blue) 40%, var(--blue-deep) 100%);
    color: #ffffff;
    font-family: "Open Sans", Calibri, sans-serif;
    font-size: 22px;
    letter-spacing: 1.2px;
    text-align: center;
    line-height: 50px;
  }
</style>
</head>
<body>
  <main class="flyer">
    <div class="headline-script">Grand Opening</div>
    <h1 class="headline-main line-one">NEW MEDICAL</h1>
    <div class="headline-main line-two">CLINIC</div>

    <svg class="connector-lines" width="975" height="30" viewBox="0 0 975 30" aria-hidden="true">
      <g stroke="var(--rule)" stroke-width="2.5">
        <line x1="0" y1="4" x2="975" y2="4"/>
        <line x1="0" y1="14" x2="975" y2="14"/>
        <line x1="0" y1="24" x2="975" y2="24"/>
      </g>
    </svg>

    <div class="badge badge-yellow">Accepting<br>Walk-in<br>Patients</div>
    <div class="badge badge-blue">OPEN<br>6 DAYS<br>A WEEK</div>
    <div class="badge badge-green">Walk-ins<br>are<br>Welcome</div>

    <div class="doctor-photo" role="img" aria-label="Photo of a smiling doctor in a white coat with a stethoscope, arms crossed, in a bright clinic"></div>

    <section class="services">
      <h2 class="services-title">OUR SERVICES ARE:</h2>
      <ul class="services-list">
        <li>Family Practice</li>
        <li>Cardiology Diagnostics</li>
        <li>Cardiac &amp; Vascular Surgical Consultation</li>
        <li>Ultrasound &amp; Vascular Testing</li>
        <li>Ample Free Parking</li>
        <li>Friendly Staffs</li>
      </ul>
    </section>

    <section class="location">
      <h2 class="location-title">LOCATION</h2>
      <p class="location-address">2957 Corliss Road West,<br>Unit 418, Scarborough,<br>Ontario, K7P 2H9</p>
    </section>

    <section class="booking">
      <p class="booking-call">CALL FOR BOOK<br>APPOINTMENT</p>
      <p class="booking-phone">(555) 384-2760</p>
    </section>

    <footer class="footer-band">Our lab is affiliated with several nuclear medicine clinics in the GTA.</footer>
  </main>
</body>
</html>
```